Business Card and Letterhead Design for Public Accounting Firm

Business card and letterhead design for a CPA Firm located in Orange County, CA. We're looking for a modern and professional design utilizing our existing logo. We'd like a clean "less is more" look, but also something that catches the eye. We provide a high level of service to our clients. Open to single or double sided business cards.

Additional info: color numbers on logo
Blue :
R 0
G 83
B 125

#00537D

Silver :

R 154
G 154
B 154

#9A9A9A

Target Market(s)

Businesses and individuals

Industry/Entity Type

Accounting

Contact Information for Business Card

Moss Whitfield & Danby LLP - 4827 Larkspur Vale Road, Irvine, CA 92614 - (949)731-2864 - mwdaccts.example

Font styles to use
Serif
Sans Serif
Other font styles liked:
• See font file uploaded

Colors
0054AA
0677BA
7BADD7
CADEEF
E8F1F8

Requirements
Nice to have
• Possibly use the font file provided which matches our logo, but adjust to be not in all caps

```html
<!DOCTYPE html>
<html lang="en">
<head>
<meta charset="utf-8">
<title>Moss Whitfield &amp; Danby LLP — Business Card</title>
<link rel="stylesheet" href="https://fonts.googleapis.com/css2?family=Cinzel:wght@400&family=Lato:wght@400;700;900&display=swap">
<style>
  :root {
    --brand-blue: #00537d;
    --brand-silver: #9a9a9a;
    --paper: #ffffff;
    --ink: #1a1a1a;
    --backdrop-top: #2b2b2b;
    --backdrop-bottom: #0d0d0d;
  }
  * { margin: 0; padding: 0; box-sizing: border-box; }
  html, body {
    width: 1200px; height: 1015px; overflow: hidden;
  }
  body {
    background: radial-gradient(ellipse at 50% 40%, var(--backdrop-top), var(--backdrop-bottom) 75%);
    font-family: "Lato", sans-serif;
    position: relative;
  }
  .card {
    position: absolute;
    width: 560px; height: 320px;
    box-shadow: 0 14px 30px rgba(0,0,0,0.55);
    overflow: hidden;
  }
  .card--back {
    left: 60px; top: 110px;
    background: var(--brand-blue);
    display: flex; align-items: center; justify-content: center;
  }
  .card--front {
    left: 580px; top: 560px;
    background: var(--paper);
  }
  .wordmark {
    display: flex; align-items: center; gap: 14px;
    font-family: "Cinzel", serif;
    font-weight: 400;
    letter-spacing: 0.18em;
    line-height: 1.25;
    font-size: 19px;
  }
  .wordmark__square {
    width: 22px; height: 22px; flex: none;
  }
  .card--back .wordmark { color: var(--paper); }
  .card--back .wordmark__square { background: var(--paper); }
  .card--front .wordmark {
    position: absolute; left: 0; right: 0; top: 62px;
    justify-content: center;
    color: var(--brand-silver);
  }
  .card--front .wordmark__square { background: var(--brand-blue); }
  .contact-band {
    position: absolute; left: 0; right: 0; top: 166px; height: 100px;
    background: var(--brand-blue);
    color: var(--paper);
    display: flex; align-items: center; justify-content: center;
  }
  .person { text-align: right; padding-right: 22px; }
  .person__name { font-weight: 900; font-size: 19px; letter-spacing: 0.02em; }
  .person__title { font-size: 14px; margin-top: 2px; }
  .band-divider { width: 1px; height: 58px; background: rgba(255,255,255,0.45); }
  .contact-list { list-style: none; padding-left: 22px; font-size: 14px; }
  .contact-list li { display: flex; align-items: center; gap: 8px; line-height: 1.6; }
  .contact-list svg { width: 14px; height: 14px; flex: none; }
  .address {
    position: absolute; left: 0; right: 0; top: 282px;
    text-align: center; font-size: 14px; color: var(--ink);
  }
</style>
</head>
<body>

<section class="card card--back" aria-label="Business card, back">
  <div class="wordmark">
    <span class="wordmark__square"></span>
    <span>Moss Whitfield<br>&amp; Danby LLP</span>
  </div>
</section>

<section class="card card--front" aria-label="Business card, front">
  <div class="wordmark">
    <span class="wordmark__square"></span>
    <span>Moss Whitfield<br>&amp; Danby LLP</span>
  </div>

  <div class="contact-band">
    <div class="person">
      <p class="person__name">ELLIS HARROW</p>
      <p class="person__title">Managing Director</p>
    </div>
    <span class="band-divider"></span>
    <ul class="contact-list">
      <li>
        <svg viewBox="0 0 24 24" aria-hidden="true"><path fill="#fff" d="M6.6 10.8a15.1 15.1 0 0 0 6.6 6.6l2.2-2.2a1 1 0 0 1 1-.25 11.4 11.4 0 0 0 3.6.57 1 1 0 0 1 1 1V20a1 1 0 0 1-1 1A17 17 0 0 1 3 4a1 1 0 0 1 1-1h3.5a1 1 0 0 1 1 1c0 1.25.2 2.45.57 3.6a1 1 0 0 1-.25 1z"/></svg>
        (949)731-2864
      </li>
      <li>
        <svg viewBox="0 0 24 24" aria-hidden="true" fill="none" stroke="#fff" stroke-width="2"><circle cx="12" cy="12" r="9"/><ellipse cx="12" cy="12" rx="4" ry="9"/><path d="M3 12h18M5 7h14M5 17h14"/></svg>
        www.mwdaccts.example
      </li>
    </ul>
  </div>

  <p class="address">4827 Larkspur Vale Road, Irvine, CA 92614</p>
</section>

</body>
</html>
```